Flyer Vacation Gift Certificate

I need to create a beautiful flyer 8.5 x 11 PDF format flyer design. <br/><br/>Instructions:<br/>The flyer will really be a gift voucher for a las vegas vacation getaway. So must have a Las Vegas Theme exciting fun<br/><br/>The voucher should have two modules that will be editable. <br/>Must have a "Compliments Of" area and also must have an "Exclusively For" area<br/><br/>Keep in mind that this flyer will be printed so keep that in mind :)<br/><br/>Here the is the content for the vacation voucher:<br/><br/>There is no doubt that Las Vegas is one of the hottest travel destinations around the world. In fact, some people would even go as far as<br/>saying that perhaps it is THE hottest place to visit. Enjoy up to 4 nights of resort/casino accommodations in exciting Las Vegas, NV. Millions of people travel to this exciting city each year to enjoy its thrills. Thanks to the business you received this certificate from, now you can enjoy exciting Las Vegas, NV too!<br/><br/>Features:<br/>*Travel 7 Days A Week<br/>*Stay Your Choice Of Nights (1-4 Nights)<br/>*Good For Two Adults & Two Children<br/>*Pay Just The Taxes & Fees<br/>*Multiple Travel Date Requests Allowed<br/>*Fully Transferable To Another Person<br/>*Just A 30 Days Advance Notice Required<br/>*You Will Have 12 Months To Complete Travel After Redemption<br/><br/>HOW CAN WE DO THIS?<br/><br/>We contract with the world leading hotel chains and resorts to help them fill their otherwise empty rooms.<br/><br/>We help fill empty rooms which the hotels, resorts and cruise lines turn into additional revenue from other areas of their property and future bookings.<br/><br/>Hotels rarely experience full occupancy, yet they remain open, providing rooms and services at fixed costs. So when hotels give out their rooms by partnering with marketing companies like us, they might miss out on the room fee, but they already didn't have that in the first place, at least now they have the opportunity to gain a customer for their in-house restaurants, room service, their casinos, an extra day stay, future bookings, etc.<br/><br/>VIEW ALL THE DETAILS OF THIS SPECIAL OFFER AND REDEEM ONLINE AT <br/>WWW.TOPAZVOUCHERDESK.COM<br/><br/>Certificate ID # 47261-38504<br/>Expires 02/29/2020<br/><br/><br/>*terms and conditions apply see website for details<br/><br/>KEEP IN MIND THE EXAMPLES I AM UPLOADING ARE SIMPLY TO SHOW YOU THAT THEY CONTAIN THE "COMPLIMENTS OF" AND "EXCLUSIVELY FOR" ELEMENTS. THESE MUST BE INCLUDED IN NEW DESIGN. PLEASE ONLY USE THE CONTENT I PROVIDED IN BRIEF, DONT USE CONTENT FROM EXAMPLES.

Target Market(s)

CONSUMERS THAT HAVE BEEN REWARDED WITH A VACATION CERTIFICATE FOR DOING BUSINESS WITH A COMPANY.

COMPANIES USE THESE AS MARKETING INCENTIVES TO ATTRACT MORE CUSTOMERS AND TO REWARD LOYALTY, ETC.

Industry/Entity Type

Travel Industry

Colors

Designer to choose colors to be used in the design.

Requirements
Must have
• I need to create a beautiful flyer 8.5 x 11 PDF format flyer design.
• Instructions:
• The flyer will really be a gift voucher for a las vegas vacation getaway. So must have a Las Vegas Theme exciting fun
• The voucher should have two modules that will be editable.
• Must have a "Compliments Of" area and also must have an "Exclusively For" area
• Keep in mind that this flyer will be printed so keep that in mind :)
• Here the is the content for the vacation voucher:
• There is no doubt that Las Vegas is one of the hottest travel destinations around the world. In fact, some people would even go as far as
• saying that perhaps it is THE hottest place to visit. Enjoy up to 4 nights of resort/casino accommodations in exciting Las Vegas, NV. Millions of people travel to this exciting city each year to enjoy its thrills. Thanks to the business you received this certificate from, now you can enjoy exciting Las Vegas, NV too!
• Features:
• *Travel 7 Days A Week
• *Stay Your Choice Of Nights (1-4 Nights)
• *Good For Two Adults & Two Children
• *Pay Just The Taxes & Fees
• *Multiple Travel Date Requests Allowed
• *Fully Transferable To Another Person
• *Just A 30 Days Advance Notice Required
• *You Will Have 12 Months To Complete Travel After Redemption
• HOW CAN WE DO THIS?
• We contract with the world leading hotel chains and resorts to help them fill their otherwise empty rooms.
• We help fill empty rooms which the hotels, resorts and cruise lines turn into additional revenue from other areas of their property and future bookings.
• Hotels rarely experience full occupancy, yet they remain open, providing rooms and services at fixed costs. So when hotels give out their rooms by partnering with marketing companies like us, they might miss out on the room fee, but they already didn't have that in the first place, at least now they have the opportunity to gain a customer for their in-house restaurants, room service, their casinos, an extra day stay, future bookings, etc.
• VIEW ALL THE DETAILS OF THIS SPECIAL OFFER AND REDEEM ONLINE AT
• WWW.TOPAZVOUCHERDESK.COM
• Certificate ID # 47261-38504
• Expires 02/29/2020
• *terms and conditions apply see website for details
• KEEP IN MIND THE EXAMPLES I AM UPLOADING ARE SIMPLY TO SHOW YOU THAT THEY CONTAIN THE "COMPLIMENTS OF" AND "EXCLUSIVELY FOR" ELEMENTS. THESE MUST BE INCLUDED IN NEW DESIGN. PLEASE ONLY USE THE CONTENT I PROVIDED IN BRIEF, DONT USE CONTENT FROM EXAMPLES.
Nice to have
• EXCITING LAS VEGAS IMAGES THAT MAKE SOMEONE WANT TO GO THERE

```html
<!DOCTYPE html>
<html lang="en">
<head>
<meta charset="utf-8">
<title>Las Vegas Vacation Getaway Gift Voucher</title>
<link href="https://fonts.googleapis.com/css2?family=Oswald:wght@500;600&family=Source+Sans+3:wght@400;600;700&display=swap" rel="stylesheet">
<style>
  :root{
    --page-bg:#d9d9d9;
    --blue:#1c4f98;
    --blue-deep:#0c2d6a;
    --red:#d0171f;
    --red-deep:#8a0e14;
    --gold:#f7b449;
    --white:#ffffff;
    --gray:#ebebec;
    --ink:#2a2a2a;
    --muted:#6d6d6d;
    --bullet:#e08a2a;
  }
  *{box-sizing:border-box;margin:0;padding:0}
  html,body{width:958px;height:1200px;overflow:hidden;background:var(--page-bg)}
  body{font-family:"Source Sans 3",Arial,sans-serif}
  .flyer{position:absolute;left:13px;top:0;width:932px;height:1200px;overflow:hidden;
    background:linear-gradient(180deg,var(--blue) 0%,var(--blue-deep) 100%)}
  .hero-photo{position:absolute;left:0;top:0;width:932px;height:470px;
    background:linear-gradient(120deg,#2a3d7a 0%,#4b6fc0 35%,#c4423b 65%,#1a2c63 100%)}
  .inset-photo{position:absolute;border:8px solid var(--white);box-shadow:0 4px 12px rgba(0,0,0,.45)}
  .inset-gondola{left:622px;top:160px;width:282px;height:340px;transform:rotate(8deg);
    background:linear-gradient(160deg,#8fb1d8 0%,#d7b58a 55%,#7a5a3d 100%)}
  .inset-casino{left:532px;top:370px;width:180px;height:170px;transform:rotate(-5deg);
    background:linear-gradient(150deg,#3a2a3e 0%,#b0573a 50%,#2f3f6a 100%)}
  .swoosh{position:absolute;left:0;top:380px;width:932px;height:100px}
  .ribbon{position:absolute;left:-58px;top:52px;width:280px;height:46px;transform:rotate(-45deg);
    background:var(--red);color:var(--white);font-family:"Oswald",sans-serif;font-weight:500;
    font-size:21px;letter-spacing:1px;text-align:center;line-height:46px;box-shadow:0 3px 6px rgba(0,0,0,.35)}
  .title{position:absolute;left:50px;top:452px;font-family:"Oswald",sans-serif;text-shadow:0 3px 6px rgba(0,0,0,.5);font-weight:400}
  .title-main{font-size:78px;line-height:88px;font-weight:600;color:var(--gold)}
  .title-sub{font-size:42px;line-height:48px;font-weight:500;color:var(--white)}
  .recipients{position:absolute;left:41px;top:600px;color:var(--white);font-size:21px;line-height:32px}
  .recipients b{font-weight:700;text-transform:uppercase}
  .intro{position:absolute;left:41px;top:672px;width:500px;color:var(--white);font-size:14.5px;line-height:20.5px;text-align:justify}
  .features{position:absolute;left:556px;top:503px;width:348px;height:379px;z-index:3;
    background:linear-gradient(180deg,var(--red) 0%,var(--red-deep) 100%);border-radius:0 0 12px 12px;
    padding:100px 10px 0 14px;color:var(--white);box-shadow:0 4px 10px rgba(0,0,0,.35)}
  .features h2{position:absolute;left:14px;top:50px;font-family:"Oswald",sans-serif;font-weight:500;font-size:32px;line-height:40px;letter-spacing:.5px}
  .features li{list-style:none;position:relative;padding-left:24px;font-size:16px;line-height:29px;font-weight:600;letter-spacing:-.1px}
  .bullet-list li::before{content:"";position:absolute;left:0;top:8px;width:13px;height:13px;border-radius:50%;border:2px solid currentColor}
  .bullet-list li::after{content:"";position:absolute;left:3px;top:12.5px;width:4px;height:4px;border-top:2px solid currentColor;border-right:2px solid currentColor;transform:rotate(45deg)}
  .how-tab{position:absolute;left:0;top:833px;width:377px;height:49px;background:linear-gradient(180deg,var(--red) 0%,var(--red-deep) 100%);
    border-radius:0 24px 24px 0;color:var(--white);font-family:"Oswald",sans-serif;font-weight:500;font-size:24px;line-height:49px;padding-left:48px;z-index:2}
  .how-panel{position:absolute;left:0;top:862px;width:932px;height:239px;background:var(--gray);padding:40px 28px 0 68px;color:var(--ink)}
  .how-panel li{list-style:none;position:relative;font-size:14.5px;line-height:19px;margin-bottom:11px}
  .how-panel li::before{left:-26px;top:3px;color:var(--bullet)}
  .how-panel li::after{left:-23px;top:7.5px;color:var(--bullet)}
  .cert-line{position:absolute;left:0;top:214px;width:100%;text-align:center;font-size:12px;color:var(--muted)}
  .redeem{position:absolute;left:41px;top:1101px;width:861px;height:50px;border-radius:25px;z-index:2;
    background:linear-gradient(180deg,var(--red) 0%,var(--red-deep) 100%);color:var(--white);
    font-family:"Oswald",sans-serif;font-weight:500;font-size:19px;line-height:50px;text-align:center;letter-spacing:.3px;box-shadow:0 3px 8px rgba(0,0,0,.35)}
  .redeem .globe{display:inline-block;width:13px;height:13px;border:2px solid var(--gold);border-radius:50%;margin:0 10px;vertical-align:-1px}
  .terms{position:absolute;left:0;top:1165px;width:100%;text-align:center;color:var(--white);font-size:14px}
</style>
</head>
<body>
<main class="flyer">
  <div class="hero-photo" role="img" aria-label="Smiling couple in front of the famous welcome sign on the Las Vegas Strip at night"></div>

  <svg class="swoosh" viewBox="0 0 932 100" preserveAspectRatio="none" aria-hidden="true">
    <path d="M0 50 C 200 10, 400 0, 560 20 L 560 100 L 0 100 Z" fill="#ffffff"/>
    <path d="M0 72 C 200 30, 400 24, 580 48 L 580 100 L 0 100 Z" fill="#c8161d"/>
    <path d="M0 82 C 200 42, 400 38, 590 62 L 932 62 L 932 100 L 0 100 Z" fill="#1c4f98"/>
  </svg>

  <div class="inset-photo inset-gondola" role="img" aria-label="Couple on a gondola ride inside a Venetian-style Las Vegas resort"></div>
  <div class="inset-photo inset-casino" role="img" aria-label="Friends celebrating at a casino roulette table"></div>

  <div class="ribbon">GIFT VOUCHER</div>

  <h1 class="title">
    <div class="title-main">LAS VEGAS</div>
    <div class="title-sub">VACATION GETAWAY</div>
  </h1>

  <div class="recipients">
    <p><b>Compliments of:</b> Two Adults &amp; Two Children</p>
    <p><b>Exclusively for:</b> Customer Name</p>
  </div>

  <p class="intro">There is no doubt that Las Vegas is one of the hottest travel destinations around the world. In fact, some people would even go as far as saying that perhaps it is THE hottest place to visit. Enjoy up to 4 nights of resort/casino accommodations in exciting Las Vegas, NV. Millions of people travel to this exciting city each year to enjoy its thrills. Thanks to the business you received this certificate from, now you can enjoy exciting Las Vegas, NV too!</p>

  <section class="features">
    <h2>FEATURES:</h2>
    <ul class="bullet-list">
      <li>Travel 7 Days A Week</li>
      <li>Stay Your Choice Of Nights (1- 4 Nights)</li>
      <li>Good For Two Adults &amp; Two Children</li>
      <li>Pay Just The Taxes &amp; Fees</li>
      <li>Multiple Travel Date Requests Allowed</li>
      <li>Fully Transferable To Another Person</li>
      <li>Just A 30 Days Advance Notice Required</li>
      <li>You Will Have 12 Months To Complete<br>Travel After Redemption</li>
    </ul>
  </section>

  <div class="how-tab">HOW CAN WE DO THIS?</div>
  <section class="how-panel">
    <ul class="bullet-list">
      <li>We contract with the world leading hotel chains and resorts to help them fill their otherwise empty rooms.</li>
      <li>We help fill empty rooms which the hotels, resorts and cruise lines turn into additional revenue from other areas of their property and future bookings.</li>
      <li>Hotels rarely experience full occupancy, yet they remain open, providing rooms and services at fixed costs. So when hotels give out their rooms by partnering with marketing companies like us, they might miss out on the room fee, but they already didn't have that in the first place, at least now they have the opportunity to gain a customer for their in-house restaurants, room service, their casinos, an extra day stay, future bookings, etc.</li>
    </ul>
    <p class="cert-line">Certificate ID # 47261-38504 &nbsp;|&nbsp; Expires 02/29/2020</p>
  </section>

  <div class="redeem">VIEW ALL THE DETAILS OF THIS SPECIAL OFFER AND REDEEM ONLINE AT<span class="globe"></span>WWW.TOPAZVOUCHERDESK.COM</div>
  <p class="terms">*terms and conditions apply see website for details</p>
</main>
</body>
</html>
```